Kelvo Auto - help to get me noticed

We not long ago tasked Pixel Harbour to design a logo for my business. I'm happy with the result so would like to have a business card designed as a follow up.

It's an Automotive service and repair business that offers the following -
- Servicing
- General repairs
- Brakes
- Detailing
- Integrity

Kelvo Automotive
Dallin Mereth
0471 926 317

Target Market(s)

Everyday people with the ability to reach out to corporate customers also.

Industry/Entity Type

Automotive

Contact Information for Business Card

Black card, logo, name and phone number on front. Other details on back of card.

```html
<!DOCTYPE html>
<html lang="en">
<head>
<meta charset="UTF-8">
<title>Kelvo Automotive — Business Cards</title>
<link href="https://fonts.googleapis.com/css2?family=Lato:wght@400;700;900&display=swap" rel="stylesheet">
<style>
  :root {
    --backdrop: #d0d0cb;
    --card-black: #121317;
    --brand-green: #7cc242;
    --edge-green: #4fae3a;
    --text-white: #f2f2f2;
  }
  * { margin: 0; padding: 0; box-sizing: border-box; }
  html, body {
    width: 1200px;
    height: 801px;
    overflow: hidden;
    background: var(--backdrop);
    font-family: "Lato", sans-serif;
  }
  .stage {
    position: relative;
    width: 1200px;
    height: 801px;
  }
  .card {
    position: absolute;
    top: 236px;
    width: 520px;
    height: 300px;
    background: var(--card-black);
    border-bottom: 4px solid var(--edge-green);
    border-right: 4px solid var(--edge-green);
    box-shadow: 0 14px 30px rgba(0, 0, 0, 0.28);
  }
  .card--contact { left: 52px; }
  .card--services { left: 628px; }

  .wordmark {
    position: absolute;
    display: flex;
    align-items: center;
    gap: 10px;
    color: var(--brand-green);
    font-weight: 900;
    text-transform: uppercase;
    line-height: 1;
    white-space: nowrap;
  }
  .wordmark__square {
    display: block;
    background: var(--brand-green);
  }
  .card--contact .wordmark {
    top: 42px;
    right: 44px;
    font-size: 24px;
    letter-spacing: 1px;
  }
  .card--contact .wordmark__square { width: 16px; height: 16px; }

  .contact {
    position: absolute;
    left: 40px;
    bottom: 40px;
  }
  .contact__name {
    color: var(--brand-green);
    font-weight: 700;
    font-size: 24px;
    letter-spacing: 0.5px;
    text-transform: uppercase;
  }
  .contact__phone {
    display: flex;
    align-items: center;
    gap: 10px;
    margin-top: 8px;
    color: var(--text-white);
    font-size: 15px;
    letter-spacing: 0.5px;
  }
  .contact__phone svg { width: 14px; height: 14px; }

  .card--services .wordmark {
    top: 96px;
    left: 50%;
    transform: translateX(-50%);
    font-size: 40px;
    letter-spacing: 1.5px;
  }
  .card--services .wordmark__square { width: 26px; height: 26px; }

  .services {
    position: absolute;
    left: 0;
    right: 0;
    bottom: 40px;
    display: flex;
    justify-content: center;
    align-items: center;
    gap: 9px;
    list-style: none;
    color: var(--text-white);
    font-size: 13px;
    letter-spacing: 1px;
    text-transform: uppercase;
  }
  .services__divider {
    width: 1px;
    height: 13px;
    background: var(--brand-green);
  }
</style>
</head>
<body>
<main class="stage">
  <section class="card card--contact" aria-label="Business card front">
    <div class="wordmark"><span class="wordmark__square"></span>Kelvo Automotive</div>
    <div class="contact">
      <p class="contact__name">Dallin Mereth</p>
      <p class="contact__phone">
        <svg viewBox="0 0 24 24" aria-hidden="true">
          <path fill="#7cc242" d="M6.6 10.8a15.1 15.1 0 0 0 6.6 6.6l2.2-2.2a1 1 0 0 1 1-.25 11.4 11.4 0 0 0 3.6.57 1 1 0 0 1 1 1V20a1 1 0 0 1-1 1A17 17 0 0 1 3 4a1 1 0 0 1 1-1h3.5a1 1 0 0 1 1 1c0 1.25.2 2.45.57 3.57a1 1 0 0 1-.25 1z"/>
        </svg>
        0471 926 317
      </p>
    </div>
  </section>

  <section class="card card--services" aria-label="Business card back">
    <div class="wordmark"><span class="wordmark__square"></span>Kelvo Automotive</div>
    <ul class="services">
      <li>Servicing</li><li class="services__divider" aria-hidden="true"></li>
      <li>General Repairs</li><li class="services__divider" aria-hidden="true"></li>
      <li>Brakes</li><li class="services__divider" aria-hidden="true"></li>
      <li>Detailing</li><li class="services__divider" aria-hidden="true"></li>
      <li>Integrity</li>
    </ul>
  </section>
</main>
</body>
</html>
```